Belle Journée Weddings and Events

I am a small boutique wedding coordinator, stylist and bridal consultant/coach/assistant. I am based in Brisbane, Australia and my business is geared towards mid range- high end budget bridal couples.
I am after some business cards that are double sided, with the logo on one side and all other information on the other side, including the business tagline of design, create, celebrate. The look of the card needs to be clean and crisp, with white and the tones of grey of the logo.The final design needs to convey sophistication and poise. Perhaps the logo and tagline could be done in a metallic silver with the rest of the text in the shades of grey from the style guide attached below.
Title- Mirela Tostavanque - Director / Events Manager and Stylist
Address - 218 Hollis Terrace, Marwick Vale, QLD, 4067
Phone- 07 3482 9517
Mobile- 0418 572 906
Email- Mirela@bellejourneeevents.com.au
Website- www.bellejourneeevents.com.au

```html
<!DOCTYPE html>
<html lang="en">
<head>
<meta charset="utf-8">
<title>Belle Journée Weddings and Events — Business Card</title>
<link rel="stylesheet" href="https://fonts.googleapis.com/css2?family=Poiret+One&family=Italianno&display=swap">
<style>
  :root {
    --page-bg: #ffffff;
    --card-black: #1e1e1e;
    --card-black-deep: #141414;
    --silver-light: #e6e6e6;
    --silver-mid: #bdbdbd;
    --silver-dark: #8f8f8f;
    --rim-dark: #3a3a3a;
    --ink-dark: #2a2a2a;
    --ink-mid: #3c3c3c;
    --logo-silver: #dcdcdc;
    --ornament-tone: #4a4a4a;
  }
  * { box-sizing: border-box; margin: 0; padding: 0; }
  html, body {
    width: 1200px;
    height: 900px;
    overflow: hidden;
    background: var(--page-bg);
  }
  .stage {
    position: relative;
    width: 1200px;
    height: 900px;
  }
  .card {
    position: absolute;
    top: 290px;
    width: 520px;
    height: 318px;
    border-radius: 24px;
    box-shadow: 0 14px 30px rgba(0,0,0,0.18);
  }

  /* Front: logo side */
  .card-front {
    left: 50px;
    padding: 7px;
    background: linear-gradient(160deg, var(--silver-light), var(--silver-dark) 45%, var(--silver-light) 70%, var(--silver-mid));
    border: 3px solid var(--rim-dark);
  }
  .card-front-inner {
    position: relative;
    width: 100%;
    height: 100%;
    border-radius: 16px;
    background: radial-gradient(ellipse at 45% 50%, var(--card-black) 0%, var(--card-black-deep) 100%);
  }
  .ornament-frame {
    position: absolute;
    left: 50%;
    top: 50%;
    width: 230px;
    height: 270px;
    transform: translate(-62%, -50%);
  }
  .logo {
    position: absolute;
    left: 45%;
    top: 50%;
    transform: translate(-50%, -50%);
    text-align: right;
    font-family: "Poiret One", sans-serif;
    color: var(--logo-silver);
  }
  .logo-name {
    display: block;
    font-size: 40px;
    line-height: 1;
    white-space: nowrap;
  }
  .logo-sub {
    display: block;
    margin-top: 6px;
    font-size: 13px;
    letter-spacing: 0.5px;
  }

  /* Back: details side */
  .card-back {
    left: 630px;
    background: linear-gradient(180deg, var(--silver-dark) 0%, var(--silver-light) 38%, var(--silver-mid) 70%, var(--silver-dark) 100%);
    font-family: "Poiret One", sans-serif;
    color: var(--ink-mid);
    text-align: center;
  }
  .person-name {
    margin-top: 46px;
    font-family: "Italianno", cursive;
    font-size: 44px;
    line-height: 1;
    color: var(--ink-dark);
  }
  .person-title {
    margin-top: 2px;
    font-size: 11px;
    font-weight: 400;
    color: var(--ink-dark);
  }
  .contact-group {
    margin-top: 20px;
    font-size: 15px;
    line-height: 21px;
  }
  .contact-group + .contact-group { margin-top: 14px; }
  .contact-address {
    margin-top: 14px;
    font-size: 14px;
  }
  .tagline {
    position: absolute;
    left: 0;
    right: 0;
    bottom: 22px;
    font-size: 13px;
    letter-spacing: 12px;
    color: var(--ink-dark);
  }
</style>
</head>
<body>
<main class="stage">
  <section class="card card-front" aria-label="Card front">
    <div class="card-front-inner">
      <svg class="ornament-frame" viewBox="0 0 230 270" role="img" aria-label="Decorative silver scroll frame around the business name">
        <defs>
          <radialGradient id="frameTone" cx="50%" cy="50%" r="50%">
            <stop offset="0%" stop-color="#2a2a2a" stop-opacity="0"/>
            <stop offset="80%" stop-color="#3a3a3a" stop-opacity="0.35"/>
            <stop offset="100%" stop-color="#4a4a4a" stop-opacity="0.55"/>
          </radialGradient>
        </defs>
        <ellipse cx="115" cy="135" rx="112" ry="132" fill="url(#frameTone)"/>
      </svg>
      <div class="logo">
        <span class="logo-name">Belle Journée</span>
        <span class="logo-sub">Weddings &amp; Events</span>
      </div>
    </div>
  </section>

  <section class="card card-back" aria-label="Card back">
    <h1 class="person-name">Mirela Tostavanque</h1>
    <p class="person-title">Director / Events Manager and Stylist</p>
    <p class="contact-group">07 3482 9517<br>0418 572 906</p>
    <p class="contact-group">Mirela@bellejourneeevents.com.au<br>www.bellejourneeevents.com.au</p>
    <p class="contact-address">218 Hollis Terrace, Marwick Vale, QLD, 4067</p>
    <p class="tagline">CREATE, CELEBRATE</p>
  </section>
</main>
</body>
</html>
```